MORVANT EU Project PowerPoint Template

Please Provide a PowerPoint template to be used for a European project. The main scope of the project is to support research organisations across Europe to design and implement gender equality plans in order to promote the women’s position of the filed of STEM research.
The Power Point template is going to be used by the entire consortium of the project (approx. 50 people) and it is going to be used to deliver official reports to the Continental Directorate and in real -life events like international Conferences etc. Therefore, the design has to be professional and official. Given that the PowerPoint template is going to be utilised by several people simultaneously, the document should afford each user to add elements (tables, etc.) that have the same format. Any time the user adds bullet points, these should have a particular colour and shape, and so on. Please note the Consortium members are both MS Windows and MAC users.
In terms of layout, please consult the colour combination of the attached logo, to design a template with matching colour patterns. Attached to this project description you may find a generic PowerPoint template for the project just as an example. Pay notice to the bottom of each slide, where a specific phrase along with the EU flag must be included. Please, keep the phrase as it is; you my find images for the EU flag here: https://velmoria.example/union/about/symbols/flag_en.
In addition, two more presentation templates from previous projects are provided as examples. You may have a good look at them too.
For any questions and/or clarifications feel free to contact.

```html
<!DOCTYPE html>
<html lang="en">
<head>
<meta charset="utf-8">
<title>MORVANT Presentation Template</title>
<link rel="stylesheet" href="https://fonts.googleapis.com/css2?family=Montserrat:wght@300;400;500;600;700&display=swap">
<style>
:root{
  --purple:#5d4ca3;
  --purple-dark:#4a3b8e;
  --purple-light:#8a7cc6;
  --yellow:#f4b41a;
  --pink:#e8577c;
  --coral:#f47e5f;
  --ink:#3b3b4a;
  --grey:#e9e9ef;
  --line:#d9d9e2;
  --page:#eef0f4;
  --white:#ffffff;
  --flag:#1f3f9a;
}
*{box-sizing:border-box;margin:0;padding:0}
html,body{width:1200px;height:2680px;overflow:hidden;background:var(--page)}
body{font-family:"Montserrat",Arial,sans-serif;color:var(--ink)}
.sheet{display:grid;grid-template-columns:575px 575px;grid-auto-rows:320px;gap:12px 14px;padding:14px 18px}
.slide{position:relative;overflow:hidden;background:var(--white);box-shadow:0 1px 3px rgba(0,0,0,.12)}
.slide--purple{background:linear-gradient(135deg,#6b5bb3,#5a4aa0 60%,#6253ab)}
.slide--yellow{background:var(--yellow)}

/* brand */
.brand{display:flex;align-items:center;gap:6px;font-weight:600;letter-spacing:1px;color:var(--purple)}
.brand__dot{width:14px;height:14px;border-radius:50%;background:var(--yellow)}
.brand--corner{position:absolute;top:14px;right:20px;font-size:11px}
.brand--light{color:var(--white)}
.brand--light .brand__dot{background:var(--white)}
.brand--large{font-size:22px;gap:10px}
.brand--large .brand__dot{width:24px;height:24px}

/* headings */
.slide-title{position:absolute;top:18px;left:26px;font-size:13px;font-weight:600;color:var(--purple);letter-spacing:.5px;text-transform:uppercase}

/* footer */
.footer{position:absolute;left:0;right:0;bottom:0;height:16px;background:var(--purple);display:flex;align-items:center}
.footer__flag{width:22px;height:14px;margin-left:8px;background:var(--flag)}
.footer__note{flex:1;margin-left:10px;font-size:4.6px;color:var(--white);white-space:nowrap}
.footer__tail{width:52px;height:16px;background:var(--yellow);display:flex;align-items:center;justify-content:flex-end;gap:4px;padding-right:6px;font-size:6px;color:var(--white);font-weight:600}
.footer__tail span.mini{width:8px;height:8px;border-radius:50%;background:var(--white)}

/* media placeholders */
.photo{position:absolute;background:linear-gradient(135deg,#cfe3ef,#eef3f7 55%,#d6cde8)}
.ribbon{position:absolute}

/* cover */
.cover__text{position:absolute;color:var(--white)}
.cover__title{font-size:26px;font-weight:500;letter-spacing:.5px;margin:14px 0 6px}
.cover__meta{font-size:11.5px;font-weight:300;line-height:1.45}

/* agenda */
.agenda{position:absolute;top:70px;left:58px;display:grid;grid-template-columns:250px 200px;row-gap:11.4px;font-size:10px}
.agenda__item{display:flex;align-items:center;gap:8px}
.agenda__dot{width:5px;height:5px;border-radius:50%;background:var(--purple)}
.agenda__tick{width:9px;height:9px}

/* text */
.body-text{position:absolute;left:26px;right:26px;top:52px;font-size:5.2px;line-height:1.38;color:#555}
.body-text p{margin-bottom:7px}
.body-text li{margin:0 0 7px 8px}
.body-text li::marker{color:var(--purple)}
.text-card{position:absolute;top:52px;width:245px;height:215px;border:1px solid var(--line);box-shadow:0 1px 3px rgba(0,0,0,.08);padding:12px 14px;font-size:5.2px;line-height:1.4;color:#555}
.text-card h3{font-size:7.5px;color:var(--purple);font-weight:600;margin-bottom:6px}
.text-card p{margin-bottom:7px}

/* section */
.section__title{position:absolute;left:38px;font-size:26px;font-weight:500;letter-spacing:.5px}

/* tables */
.table{position:absolute;border-collapse:collapse;font-size:6.5px;text-align:center}
.table th{height:26px;color:var(--white);font-weight:600}
.table td{height:28.5px;border-bottom:1px solid var(--line)}
.th-purple{background:var(--purple)}
.th-yellow{background:var(--yellow)}
.th-pink{background:var(--pink)}
.td-purple{background:var(--purple);color:var(--white)}

/* feature columns */
.features{position:absolute;top:52px;left:0;right:0;height:158px;display:grid;grid-template-columns:repeat(4,1fr)}
.feature{padding:14px 12px;color:var(--white);text-align:center}
.feature h4{font-size:10px;font-weight:600;margin:8px 0 4px}
.feature p{font-size:6.6px;line-height:1.35;text-align:justify}
.feature__icon{width:26px;height:26px;margin:0 auto;border:1.5px solid var(--white);border-radius:50%;display:flex;align-items:center;justify-content:center}
.bg-purple{background:var(--purple)}
.bg-yellow{background:var(--yellow)}
.bg-pink{background:var(--pink)}
.bg-coral{background:var(--coral)}

/* list panel */
.panel{position:absolute;top:74px;left:26px;right:26px;height:140px;background:var(--purple);display:flex;padding:10px 12px}
.panel__list{flex:1;list-style:none;display:flex;flex-direction:column;justify-content:space-around}
.panel__list li{display:flex;align-items:center;gap:10px;color:var(--white);font-size:6.6px;line-height:1.3}
.panel__bullet{flex:none;width:14px;height:14px;border-radius:50%;background:var(--yellow)}

/* mosaic */
.mosaic{position:absolute;top:50px;left:26px;right:26px;height:208px;display:grid;grid-template-columns:repeat(3,1fr);grid-template-rows:1fr 1fr;gap:6px}
.mosaic__cell{position:relative;display:flex;flex-direction:column;align-items:center;justify-content:center;text-align:center;color:var(--white);padding:0 12px}
.mosaic__cell h4{font-size:9px;font-weight:600;margin-bottom:5px}
.mosaic__cell p{font-size:5.4px;line-height:1.35}
.mosaic .photo{position:static;width:100%;height:100%}

/* infographic */
.info__stat{position:absolute;font-size:5.4px;line-height:1.35;color:#666;width:78px}
.info__stat b{display:block;font-size:8px;color:var(--ink);font-weight:600}
</style>
</head>
<body>
<main class="sheet">

<!-- 1 cover A -->
<section class="slide slide--purple">
  <div class="ribbon" role="img" aria-label="Curved yellow and lilac ribbon artwork" style="left:250px;top:90px;width:190px;height:230px;border-radius:60% 40% 0 0;background:linear-gradient(160deg,rgba(244,180,26,.85),rgba(200,170,110,.6) 55%,rgba(140,125,200,.5))"></div>
  <div class="cover__text" style="left:26px;top:30px">
    <div class="brand brand--light brand--large">
      <span class="brand__dot"></span>MORVANT</div>
    <h1 class="cover__title">PRESENTATION TITLE</h1>
    <p class="cover__meta">Meeting title:<br>Presenter name:<br>Presenter organisation:<br>Date:</p>
  </div>
</section>

<!-- 2 cover B -->
<section class="slide slide--purple">
  <div class="ribbon" role="img" aria-label="Curved yellow and lilac ribbon artwork" style="left:330px;top:0;width:245px;height:110px;border-radius:0 0 0 80%;background:linear-gradient(200deg,rgba(244,180,26,.85),rgba(190,170,120,.55) 55%,rgba(140,125,200,.4))"></div>
  <div class="cover__text" style="left:26px;top:118px">
    <div class="brand brand--light brand--large">
      <span class="brand__dot"></span>MORVANT</div>
    <h1 class="cover__title">PRESENTATION TITLE</h1>
    <p class="cover__meta">Meeting title:<br>Presenter name:<br>Presenter organisation:<br>Date:</p>
  </div>
</section>

<!-- 3 agenda dots -->
<section class="slide">
  <h2 class="slide-title">Our Agenda</h2>
  <div class="brand brand--corner"><span class="brand__dot"></span>MORVANT</div>
  <ul class="agenda">
    <li class="agenda__item"><span class="agenda__dot"></span>Agenda 1</li><li class="agenda__item"><span class="agenda__dot"></span>Agenda 1</li>
    <li class="agenda__item"><span class="agenda__dot"></span>Agenda 1</li><li class="agenda__item"><span class="agenda__dot"></span>Agenda 1</li>
    <li class="agenda__item"><span class="agenda__dot"></span>Agenda 1</li><li class="agenda__item"><span class="agenda__dot"></span>Agenda 1</li>
    <li class="agenda__item"><span class="agenda__dot"></span>Agenda 1</li><li class="agenda__item"><span class="agenda__dot"></span>Agenda 1</li>
    <li class="agenda__item"><span class="agenda__dot"></span>Agenda 1</li><li class="agenda__item"><span class="agenda__dot"></span>Agenda 1</li>
    <li class="agenda__item"><span class="agenda__dot"></span>Agenda 1</li><li class="agenda__item"><span class="agenda__dot"></span>Agenda 1</li>
    <li class="agenda__item"><span class="agenda__dot"></span>Agenda 1</li><li class="agenda__item"><span class="agenda__dot"></span>Agenda 1</li>
    <li class="agenda__item"><span class="agenda__dot"></span>Agenda 1</li><li class="agenda__item"><span class="agenda__dot"></span>Agenda 1</li>
  </ul>
  <footer class="footer"><span class="footer__flag"></span><span class="footer__note">This project has received funding from the Continental Directorate research and innovation programme under grant agreement No 000000.</span><span class="footer__tail"><span class="mini"></span>2</span></footer>
</section>

<!-- 4 agenda ticks -->
<section class="slide">
  <h2 class="slide-title">Our Agenda</h2>
  <div class="brand brand--corner"><span class="brand__dot"></span>MORVANT</div>
  <ul class="agenda" style="grid-template-columns:1fr">
    <li class="agenda__item"><svg class="agenda__tick" viewBox="0 0 10 10"><path d="M1 5.5l2.6 2.6L9 2" fill="none" stroke="#5d4ca3" stroke-width="1.8"/></svg>Agenda 1</li>
    <li class="agenda__item"><svg class="agenda__tick" viewBox="0 0 10 10"><path d="M1 5.5l2.6 2.6L9 2" fill="none" stroke="#5d4ca3" stroke-width="1.8"/></svg>Agenda 1</li>
    <li class="agenda__item"><svg class="agenda__tick" viewBox="0 0 10 10"><path d="M1 5.5l2.6 2.6L9 2" fill="none" stroke="#5d4ca3" stroke-width="1.8"/></svg>Agenda 1</li>
    <li class="agenda__item"><svg class="agenda__tick" viewBox="0 0 10 10"><path d="M1 5.5l2.6 2.6L9 2" fill="none" stroke="#5d4ca3" stroke-width="1.8"/></svg>Agenda 1</li>
    <li class="agenda__item"><svg class="agenda__tick" viewBox="0 0 10 10"><path d="M1 5.5l2.6 2.6L9 2" fill="none" stroke="#5d4ca3" stroke-width="1.8"/></svg>Agenda 1</li>
    <li class="agenda__item"><svg class="agenda__tick" viewBox="0 0 10 10"><path d="M1 5.5l2.6 2.6L9 2" fill="none" stroke="#5d4ca3" stroke-width="1.8"/></svg>Agenda 1</li>
    <li class="agenda__item"><svg class="agenda__tick" viewBox="0 0 10 10"><path d="M1 5.5l2.6 2.6L9 2" fill="none" stroke="#5d4ca3" stroke-width="1.8"/></svg>Agenda 1</li>
    <li class="agenda__item"><svg class="agenda__tick" viewBox="0 0 10 10"><path d="M1 5.5l2.6 2.6L9 2" fill="none" stroke="#5d4ca3" stroke-width="1.8"/></svg>Agenda 1</li>
  </ul>
  <footer class="footer"><span class="footer__flag"></span><span class="footer__note">This project has received funding from the Continental Directorate research and innovation programme under grant agreement No 000000.</span><span class="footer__tail"><span class="mini"></span>3</span></footer>
</section>

<!-- 5 heading and text -->
<section class="slide">
  <h2 class="slide-title">Heading and Text Slide</h2>
  <div class="brand brand--corner"><span class="brand__dot"></span>MORVANT</div>
  <div class="body-text">
    <p>Lorem ipsum dolor sit amet, consectetur adipiscing elit, sed do eiusmod tempor incididunt ut labore et dolore magna aliqua. Ut enim ad minim veniam, quis nostrud exercitation ullamco laboris nisi ut aliquip ex ea commodo consequat. Duis aute irure dolor in reprehenderit in voluptate velit esse cillum dolore eu fugiat nulla pariatur. Excepteur sint occaecat cupidatat non proident, sunt in culpa qui officia deserunt mollit anim id est laborum. Sed ut perspiciatis unde omnis iste natus error sit voluptatem accusantium doloremque laudantium, totam rem aperiam eaque ipsa quae ab illo inventore veritatis et quasi architecto beatae vitae dicta sunt explicabo nemo enim ipsam voluptatem.</p>
    <p>Lorem ipsum dolor sit amet, consectetur adipiscing elit, sed do eiusmod tempor incididunt ut labore et dolore magna aliqua. Ut enim ad minim veniam, quis nostrud exercitation ullamco laboris nisi ut aliquip ex ea commodo consequat. Duis aute irure dolor in reprehenderit in voluptate velit esse cillum dolore eu fugiat nulla pariatur. Excepteur sint occaecat cupidatat non proident, sunt in culpa qui officia deserunt mollit anim id est laborum. Sed ut perspiciatis unde omnis iste natus error sit voluptatem accusantium doloremque laudantium, totam rem aperiam eaque ipsa quae ab illo inventore veritatis et quasi architecto beatae vitae dicta sunt explicabo nemo enim ipsam voluptatem.</p>
    <p>Lorem ipsum dolor sit amet, consectetur adipiscing elit, sed do eiusmod tempor incididunt ut labore et dolore magna aliqua. Ut enim ad minim veniam, quis nostrud exercitation ullamco laboris nisi ut aliquip ex ea commodo consequat. Duis aute irure dolor in reprehenderit in voluptate velit esse cillum dolore eu fugiat nulla pariatur. Excepteur sint occaecat cupidatat non proident, sunt in culpa qui officia deserunt mollit anim id est laborum. Sed ut perspiciatis unde omnis iste natus error sit voluptatem accusantium doloremque laudantium, totam rem aperiam eaque ipsa quae ab illo inventore veritatis et quasi architecto beatae vitae dicta sunt explicabo nemo enim ipsam voluptatem.</p>
    <p>Lorem ipsum dolor sit amet, consectetur adipiscing elit, sed do eiusmod tempor incididunt ut labore et dolore magna aliqua. Ut enim ad minim veniam, quis nostrud exercitation ullamco laboris nisi ut aliquip ex ea commodo consequat. Duis aute irure dolor in reprehenderit in voluptate velit esse cillum dolore eu fugiat nulla pariatur. Excepteur sint occaecat cupidatat non proident, sunt in culpa qui officia deserunt mollit anim id est laborum. Sed ut perspiciatis unde omnis iste natus error sit voluptatem accusantium doloremque laudantium, totam rem aperiam eaque ipsa quae ab illo inventore veritatis et quasi architecto beatae vitae dicta sunt explicabo nemo enim ipsam voluptatem.</p>
  </div>
  <footer class="footer"><span class="footer__flag"></span><span class="footer__note">This project has received funding from the Continental Directorate research and innovation programme under grant agreement No 000000.</span><span class="footer__tail"><span class="mini"></span>4</span></footer>
</section>

<!-- 6 heading and bullets -->
<section class="slide">
  <h2 class="slide-title">Heading and Text Slide</h2>
  <div class="brand brand--corner"><span class="brand__dot"></span>MORVANT</div>
  <ul class="body-text">
    <li>Lorem ipsum dolor sit amet, consectetur adipiscing elit, sed do eiusmod tempor incididunt ut labore et dolore magna aliqua. Ut enim ad minim veniam, quis nostrud exercitation ullamco laboris nisi ut aliquip ex ea commodo consequat. Duis aute irure dolor in reprehenderit in voluptate velit esse cillum dolore eu fugiat nulla pariatur. Excepteur sint occaecat cupidatat non proident, sunt in culpa qui officia deserunt mollit anim id est laborum. Sed ut perspiciatis unde omnis iste natus error sit voluptatem accusantium doloremque laudantium totam rem aperiam.</li>
    <li>Lorem ipsum dolor sit amet, consectetur adipiscing elit, sed do eiusmod tempor incididunt ut labore et dolore magna aliqua. Ut enim ad minim veniam, quis nostrud exercitation ullamco laboris nisi ut aliquip ex ea commodo consequat. Duis aute irure dolor in reprehenderit in voluptate velit esse cillum dolore eu fugiat nulla pariatur. Excepteur sint occaecat cupidatat non proident, sunt in culpa qui officia deserunt mollit anim id est laborum. Sed ut perspiciatis unde omnis iste natus error sit voluptatem accusantium doloremque laudantium totam rem aperiam.</li>
    <li>Lorem ipsum dolor sit amet, consectetur adipiscing elit, sed do eiusmod tempor incididunt ut labore et dolore magna aliqua. Ut enim ad minim veniam, quis nostrud exercitation ullamco laboris nisi ut aliquip ex ea commodo consequat. Duis aute irure dolor in reprehenderit in voluptate velit esse cillum dolore eu fugiat nulla pariatur. Excepteur sint occaecat cupidatat non proident, sunt in culpa qui officia deserunt mollit anim id est laborum. Sed ut perspiciatis unde omnis iste natus error sit voluptatem accusantium doloremque laudantium totam rem aperiam.</li>
    <li>Lorem ipsum dolor sit amet, consectetur adipiscing elit, sed do eiusmod tempor incididunt ut labore et dolore magna aliqua. Ut enim ad minim veniam, quis nostrud exercitation ullamco laboris nisi ut aliquip ex ea commodo consequat. Duis aute irure dolor in reprehenderit in voluptate velit esse cillum dolore eu fugiat nulla pariatur. Excepteur sint occaecat cupidatat non proident, sunt in culpa qui officia deserunt mollit anim id est laborum. Sed ut perspiciatis unde omnis iste natus error sit voluptatem accusantium doloremque laudantium totam rem aperiam.</li>
    <li>Lorem ipsum dolor sit amet, consectetur adipiscing elit, sed do eiusmod tempor incididunt ut labore et dolore magna aliqua. Ut enim ad minim veniam, quis nostrud exercitation ullamco laboris nisi ut aliquip ex ea commodo consequat. Duis aute irure dolor in reprehenderit in voluptate velit esse cillum dolore eu fugiat nulla pariatur. Excepteur sint occaecat cupidatat non proident, sunt in culpa qui officia deserunt mollit anim id est laborum. Sed ut perspiciatis unde omnis iste natus error sit voluptatem accusantium doloremque laudantium totam rem aperiam.</li>
  </ul>
  <footer class="footer"><span class="footer__flag"></span><span class="footer__note">This project has received funding from the Continental Directorate research and innovation programme under grant agreement No 000000.</span><span class="footer__tail"><span class="mini"></span>5</span></footer>
</section>

<!-- 7 heading and two texts -->
<section class="slide">
  <h2 class="slide-title">Heading and 2 Text Slide</h2>
  <div class="brand brand--corner"><span class="brand__dot"></span>MORVANT</div>
  <article class="text-card" style="left:26px">
    <h3>Heading Here</h3>
    <p>Lorem ipsum dolor sit amet, consectetur adipiscing elit, sed do eiusmod tempor incididunt ut labore et dolore magna aliqua. Ut enim ad minim veniam, quis nostrud exercitation ullamco laboris nisi ut aliquip ex ea commodo consequat. Duis aute irure dolor in reprehenderit in voluptate velit esse cillum dolore eu fugiat nulla pariatur. Excepteur sint occaecat cupidatat non proident, sunt in culpa qui officia deserunt mollit anim id est laborum sed ut perspiciatis.</p>
    <p>Lorem ipsum dolor sit amet, consectetur adipiscing elit, sed do eiusmod tempor incididunt ut labore et dolore magna aliqua. Ut enim ad minim veniam, quis nostrud exercitation ullamco laboris nisi ut aliquip ex ea commodo consequat. Duis aute irure dolor in reprehenderit in voluptate velit esse cillum dolore eu fugiat nulla pariatur. Excepteur sint occaecat cupidatat non proident, sunt in culpa qui officia deserunt mollit anim id est laborum sed ut perspiciatis.</p>
  </article>
  <article class="text-card" style="left:302px">
    <h3>Heading Here</h3>
    <p>Lorem ipsum dolor sit amet, consectetur adipiscing elit, sed do eiusmod tempor incididunt ut labore et dolore magna aliqua. Ut enim ad minim veniam, quis nostrud exercitation ullamco laboris nisi ut aliquip ex ea commodo consequat. Duis aute irure dolor in reprehenderit in voluptate velit esse cillum dolore eu fugiat nulla pariatur. Excepteur sint occaecat cupidatat non proident, sunt in culpa qui officia deserunt mollit anim id est laborum sed ut perspiciatis.</p>
    <p>Lorem ipsum dolor sit amet, consectetur adipiscing elit, sed do eiusmod tempor incididunt ut labore et dolore magna aliqua. Ut enim ad minim veniam, quis nostrud exercitation ullamco laboris nisi ut aliquip ex ea commodo consequat. Duis aute irure dolor in reprehenderit in voluptate velit esse cillum dolore eu fugiat nulla pariatur. Excepteur sint occaecat cupidatat non proident, sunt in culpa qui officia deserunt mollit anim id est laborum sed ut perspiciatis.</p>
  </article>
  <footer class="footer"><span class="footer__flag"></span><span class="footer__note">This project has received funding from the Continental Directorate research and innovation programme under grant agreement No 000000.</span><span class="footer__tail"><span class="mini"></span>6</span></footer>
</section>

<!-- 8 section yellow -->
<section class="slide slide--yellow">
  <div class="photo" role="img" aria-label="Photo of a researcher pipetting in a laboratory, with curved ribbon overlay" style="left:200px;top:0;width:375px;height:320px;background:linear-gradient(100deg,rgba(244,180,26,1),rgba(244,200,120,.75) 35%,rgba(236,226,214,.85) 70%,rgba(215,180,190,.8))"></div>
  <div class="brand brand--light brand--large" style="position:absolute;left:38px;top:118px"><span class="brand__dot"></span>MORVANT</div>
  <h2 class="section__title" style="top:160px;color:var(--white)">SECTION TITLE</h2>
</section>

<!-- 9 section light -->
<section class="slide">
  <div class="photo" role="img" aria-label="Soft-focus photo of a researcher with laboratory equipment and curved ribbon overlay" style="inset:0;background:linear-gradient(100deg,#ffffff 30%,#e6eef3 55%,#d8e1ea 75%,#e4c8cf)"></div>
  <div class="brand brand--large" style="position:absolute;left:38px;top:120px"><span class="brand__dot"></span>MORVANT</div>
  <h2 class="section__title" style="top:162px;color:var(--purple)">SECTION TITLE</h2>
</section>

<!-- 10 table 1 -->
<section class="slide">
  <h2 class="slide-title">Our Table #1</h2>
  <div class="brand brand--corner"><span class="brand__dot"></span>MORVANT</div>
  <table class="table" style="left:26px;top:52px;width:250px">
    <tr><th class="th-purple" style="width:46%;text-align:left;padding-left:10px">Your Project</th><th class="th-yellow">Text 01</th><th class="th-pink">Text 02</th></tr>
    <tr><td style="text-align:left;padding-left:10px">Short Text In Here</td><td>56.5</td><td>56.5</td></tr>
    <tr><td style="text-align:left;padding-left:10px">Short Text In Here</td><td>56.5</td><td>56.5</td></tr>
    <tr><td style="text-align:left;padding-left:10px">Short Text In Here</td><td>56.5</td><td>56.5</td></tr>
    <tr><td style="text-align:left;padding-left:10px">Short Text In Here</td><td>56.5</td><td>56.5</td></tr>
    <tr><td style="text-align:left;padding-left:10px">Short Text In Here</td><td>56.5</td><td>56.5</td></tr>
    <tr><td style="text-align:left;padding-left:10px">Short Text In Here</td><td>56.5</td><td>56.5</td></tr>
  </table>
  <table class="table" style="left:300px;top:52px;width:250px">
    <tr><th class="th-purple" style="width:46%;text-align:left;padding-left:10px">Your Project</th><th class="th-yellow">Text 01</th><th class="th-pink">Text 02</th></tr>
    <tr><td style="text-align:left;padding-left:10px">Short Text In Here</td><td>56.5</td><td>56.5</td></tr>
    <tr><td style="text-align:left;padding-left:10px">Short Text In Here</td><td>56.5</td><td>56.5</td></tr>
    <tr><td style="text-align:left;padding-left:10px">Short Text In Here</td><td>56.5</td><td>56.5</td></tr>
    <tr><td style="text-align:left;padding-left:10px">Short Text In Here</td><td>56.5</td><td>56.5</td></tr>
    <tr><td style="text-align:left;padding-left:10px">Short Text In Here</td><td>56.5</td><td>56.5</td></tr>
    <tr><td style="text-align:left;padding-left:10px">Short Text In Here</td><td>56.5</td><td>56.5</td></tr>
  </table>
  <footer class="footer"><span class="footer__flag"></span><span class="footer__note">This project has received funding from the Continental Directorate research and innovation programme under grant agreement No 000000.</span><span class="footer__tail"><span class="mini"></span>9</span></footer>
</section>

<!-- 11 table 2 -->
<section class="slide">
  <h2 class="slide-title">Our Table #2</h2>
  <div class="brand brand--corner"><span class="brand__dot"></span>MORVANT</div>
  <table class="table" style="left:26px;top:52px;width:523px">
    <tr><th class="th-pink">Your Project</th><th class="th-yellow">Your Project</th><th class="th-purple">#56</th><th class="th-yellow">Your Project</th><th class="th-pink">Your Project</th></tr>
    <tr><td>Short Text</td><td>Short Text</td><td class="td-purple">56.5</td><td>Short Text</td><td>Short Text</td></tr>
    <tr><td>Short Text</td><td>Short Text</td><td class="td-purple">85.2</td><td>Short Text</td><td>Short Text</td></tr>
    <tr><td>Short Text</td><td>Short Text</td><td class="td-purple">36.2</td><td>Short Text</td><td>Short Text</td></tr>
    <tr><td>Short Text</td><td>Short Text</td><td class="td-purple">33.5</td><td>Short Text</td><td>Short Text</td></tr>
    <tr><td>Short Text</td><td>Short Text</td><td class="td-purple">21.3</td><td>Short Text</td><td>Short Text</td></tr>
    <tr><td>Short Text</td><td>Short Text</td><td class="td-purple">54.3</td><td>Short Text</td><td>Short Text</td></tr>
  </table>
  <footer class="footer"><span class="footer__flag"></span><span class="footer__note">This project has received funding from the Continental Directorate research and innovation programme under grant agreement No 000000.</span><span class="footer__tail"><span class="mini"></span>10</span></footer>
</section>

<!-- 12 feature columns -->
<section class="slide">
  <h2 class="slide-title">Your Title Here</h2>
  <div class="brand brand--corner"><span class="brand__dot"></span>MORVANT</div>
  <div class="features">
    <div class="feature bg-purple">
      <div class="feature__icon"><svg width="12" height="12" viewBox="0 0 12 12"><circle cx="6" cy="6" r="4.5" fill="none" stroke="#fff" stroke-width="1.2"/><path d="M1.5 6h9M6 1.5c2 2.5 2 6.5 0 9M6 1.5c-2 2.5-2 6.5 0 9" fill="none" stroke="#fff" stroke-width=".9"/></svg></div>
      <h4>Heading Here</h4>
      <p>Lorem ipsum dolor sit amet, consectetur adipiscing elit, sed do eiusmod tempor incididunt ut labore et dolore magna aliqua. Ut enim ad minim veniam, quis nostrud exercitation ullamco laboris nisi ut aliquip ex ea commodo consequat.</p>
    </div>
    <div class="feature bg-yellow">
      <div class="feature__icon"><svg width="12" height="12" viewBox="0 0 12 12"><path d="M6 1.5a3.2 3.2 0 0 0-2 5.7V9h4V7.2a3.2 3.2 0 0 0-2-5.7zM4.5 10.5h3" fill="none" stroke="#fff" stroke-width="1.1"/></svg></div>
      <h4>Heading Here</h4>
      <p>Lorem ipsum dolor sit amet, consectetur adipiscing elit, sed do eiusmod tempor incididunt ut labore et dolore magna aliqua. Ut enim ad minim veniam, quis nostrud exercitation ullamco laboris nisi ut aliquip ex ea commodo consequat.</p>
    </div>
    <div class="feature bg-pink">
      <div class="feature__icon"><svg width="12" height="12" viewBox="0 0 12 12"><circle cx="6" cy="6" r="2" fill="none" stroke="#fff" stroke-width="1.1"/><path d="M6 1v2M6 9v2M1 6h2M9 6h2M2.5 2.5l1.4 1.4M8.1 8.1l1.4 1.4M2.5 9.5l1.4-1.4M8.1 3.9l1.4-1.4" stroke="#fff" stroke-width="1.1"/></svg></div>
      <h4>Heading Here</h4>
      <p>Lorem ipsum dolor sit amet, consectetur adipiscing elit, sed do eiusmod tempor incididunt ut labore et dolore magna aliqua. Ut enim ad minim veniam, quis nostrud exercitation ullamco laboris nisi ut aliquip ex ea commodo consequat.</p>
    </div>
    <div class="feature bg-coral">
      <div class="feature__icon"><svg width="12" height="12" viewBox="0 0 12 12"><rect x="1.5" y="2.5" width="9" height="6.5" fill="none" stroke="#fff" stroke-width="1.1"/><path d="M4 11h4M3.5 5h5M3.5 7h3" stroke="#fff" stroke-width="1"/></svg></div>
      <h4>Heading Here</h4>
      <p>Lorem ipsum dolor sit amet, consectetur adipiscing elit, sed do eiusmod tempor incididunt ut labore et dolore magna aliqua. Ut enim ad minim veniam, quis nostrud exercitation ullamco laboris nisi ut aliquip ex ea commodo consequat.</p>
    </div>
  </div>
  <footer class="footer"><span class="footer__flag"></span><span class="footer__note">This project has received funding from the Continental Directorate research and innovation programme under grant agreement No 000000.</span><span class="footer__tail"><span class="mini"></span>11</span></footer>
</section>

<!-- 13 list panel with photo -->
<section class="slide">
  <h2 class="slide-title">Your Title Here</h2>
  <div class="brand brand--corner"><span class="brand__dot"></span>MORVANT</div>
  <div class="panel">
    <ul class="panel__list">
      <li><span class="panel__bullet"></span>Lorem ipsum dolor sit amet, consectetur adipiscing<br>elit, sed do eiusmod tempor incididunt ut labore.</li>
      <li><span class="panel__bullet"></span>Duis aute irure dolor in reprehenderit in voluptate<br>velit esse cillum dolore.</li>
      <li><span class="panel__bullet"></span>Lorem ipsum dolor sit amet, consectetur adipiscing<br>elit, sed do eiusmod tempor incididunt ut labore.</li>
      <li><span class="panel__bullet"></span>Duis aute irure dolor in reprehenderit in voluptate<br>velit esse cillum dolore.</li>
    </ul>
    <div class="photo" role="img" aria-label="Photo of a scientist at a microscope with overlaid science icons" style="position:static;width:215px;height:120px;background:linear-gradient(120deg,#f1f1f3,#cfe1e8 50%,#e9d6de)"></div>
  </div>
  <footer class="footer"><span class="footer__flag"></span><span class="footer__note">This project has received funding from the Continental Directorate research and innovation programme under grant agreement No 000000.</span><span class="footer__tail"><span class="mini"></span>12</span></footer>
</section>

<!-- 14 mosaic -->
<section class="slide">
  <h2 class="slide-title">Your Title Here</h2>
  <div class="brand brand--corner"><span class="brand__dot"></span>MORVANT</div>
  <div class="mosaic">
    <div class="photo" role="img" aria-label="Photo of gloved hands handling lab samples" style="background:linear-gradient(135deg,#7fc4e6,#cfe9f5)"></div>
    <div class="mosaic__cell bg-yellow"><h4>Heading Goes Here</h4><p>Lorem ipsum dolor sit amet, consectetur adipiscing elit, sed do eiusmod tempor incididunt ut labore et dolore magna aliqua.</p></div>
    <div class="photo" role="img" aria-label="Photo of a researcher in a laboratory" style="background:linear-gradient(135deg,#e8eef2,#c9dbe6)"></div>
    <div class="mosaic__cell bg-purple"><h4>Heading Goes Here</h4><p>Lorem ipsum dolor sit amet, consectetur adipiscing elit, sed do eiusmod tempor incididunt ut labore et dolore magna aliqua.</p></div>
    <div class="photo" role="img" aria-label="Photo of a scientist at a microscope" style="background:linear-gradient(135deg,#f0e6ea,#d3e4ec)"></div>
    <div class="mosaic__cell bg-pink"><h4>Heading Goes Here</h4><p>Lorem ipsum dolor sit amet, consectetur adipiscing elit, sed do eiusmod tempor incididunt ut labore et dolore magna aliqua.</p></div>
  </div>
  <footer class="footer"><span class="footer__flag"></span><span class="footer__note">This project has received funding from the Continental Directorate research and innovation programme under grant agreement No 000000.</span><span class="footer__tail"><span class="mini"></span>13</span></footer>
</section>

<!-- 15 infographic -->
<section class="slide">
  <h2 class="slide-title">Infographic</h2>
  <div class="brand brand--corner"><span class="brand__dot"></span>MORVANT</div>
  <svg style="position:absolute;left:0;top:0" width="575" height="320" viewBox="0 0 575 320">
    <path d="M238 304a50 50 0 0 1 100 0" fill="none" stroke="#dcdce2" stroke-width="22"/>
    <path d="M288 254l-36-60M288 254l-72 16M288 254l36-60M288 254l72 16" stroke="#cfcfd8" stroke-width="5"/>
    <circle cx="288" cy="286" r="16" fill="#ffffff" stroke="#cfcfd8" stroke-width="3"/>
    <circle cx="288" cy="286" r="6" fill="#5d4ca3"/>
    <circle cx="208" cy="254" r="22" fill="#5d4ca3"/>
    <circle cx="252" cy="180" r="26" fill="#f4b41a"/>
    <circle cx="324" cy="180" r="26" fill="#e8577c"/>
    <circle cx="368" cy="254" r="22" fill="#f47e5f"/>
    <path d="M200 254h16M208 246v16" stroke="#fff" stroke-width="2.5"/>
    <path d="M244 190l8-18 8 18M247 184h10" fill="none" stroke="#fff" stroke-width="2.5"/>
    <rect x="314" y="174" width="20" height="14" rx="2" fill="none" stroke="#fff" stroke-width="2.5"/>
    <path d="M360 246l16 16M376 246l-16 16" stroke="#fff" stroke-width="2.5"/>
    <path d="M196 152h44M336 152h44M150 236h44M382 236h44" stroke="#cfcfd8" stroke-width="1"/>
  </svg>
  <p class="info__stat" style="left:150px;top:134px;text-align:right"><b>96%</b>This is a template text. You may add your text here.</p>
  <p class="info__stat" style="left:348px;top:134px"><b>37%</b>This is a template text. You may add your text here.</p>
  <p class="info__stat" style="left:104px;top:218px;text-align:right"><b>78%</b>This is a template text. You may add your text here.</p>
  <p class="info__stat" style="left:396px;top:218px"><b>47%</b>This is a template text. You may add your text here.</p>
  <footer class="footer"><span class="footer__flag"></span><span class="footer__note">This project has received funding from the Continental Directorate research and innovation programme under grant agreement No 000000.</span><span class="footer__tail"><span class="mini"></span>14</span></footer>
</section>

<!-- 16 closing -->
<section class="slide slide--purple">
  <div class="photo" role="img" aria-label="Photo of a researcher with a pipette, framed by curved ribbons" style="left:330px;top:120px;width:245px;height:200px;border-radius:70% 0 0 0;background:linear-gradient(150deg,rgba(140,125,200,.4),rgba(230,180,200,.7) 60%,rgba(120,200,230,.7))"></div>
  <div class="brand brand--light brand--large" style="position:absolute;left:26px;top:104px"><span class="brand__dot"></span>MORVANT</div>
  <h2 class="section__title" style="left:26px;top:150px;color:var(--white)">THANK YOU</h2>
</section>

</main>
</body>
</html>
```